ZEPRILO.COM is a premium domain sales company. Our competitors are companies like vastplots.example, getparcels.example, peerwords.example. Our current site is at www.zeprilos.example.

We want to have the ability to search for domains, to highlight special offers and have some testimonials on the index page.

The logo for the site is attached.

Please be sure that the order form fits on the screen without scrolling the page. I want the entire form, including the submit button to fit without any page scrolling.

Delivered product - INDEX PAGE, ORDER FORM AND CONTENT PAGE PSDs.

Target Market(s)

Small to Medium business professionals

Industry/Entity Type

It Company

Requirements
Must have
• 1. List of domains for sale
2. Simple search box with button to run the search
3. link for advanced search
4. testimonial area. Note - this can be a small box where a different testimonial is displayed on each page load.
Nice to have
• Would like the site to have some white space. Don't want a heavily packed website. Give it an "airy" feel.

```html
<!DOCTYPE html>
<html lang="en">
<head>
<meta charset="utf-8">
<title>ZEPRILO.COM – Premium Domains</title>
<link rel="stylesheet" href="https://fonts.googleapis.com/css2?family=Open+Sans:ital,wght@0,400;0,600;0,700;1,400&family=Roboto+Condensed:wght@400&family=Ubuntu:wght@400;500;700&family=Ubuntu+Condensed&display=swap">
<style>
:root{
  --blue:#0b5aa6;
  --blue-dark:#084d91;
  --green:#84b326;
  --green-dark:#6c9a1a;
  --orange:#f28c1e;
  --text:#444;
  --muted:#666;
  --quote:#4a9de0;
}
*{box-sizing:border-box;margin:0;padding:0}
html,body{width:1120px;height:1200px;overflow:hidden;background:#fff}
body{position:relative;font-family:"Open Sans",sans-serif;color:var(--text)}
.abs{position:absolute}

/* header */
.site-header{position:absolute;left:0;top:0;width:1120px;height:90px;border-bottom:3px solid var(--green)}
.brand{left:182px;top:30px;font-family:"Ubuntu",sans-serif;font-weight:700;font-size:30px;color:var(--blue);letter-spacing:-.5px;display:flex;align-items:center;gap:8px}
.brand .dot{width:12px;height:12px;border-radius:50%;background:var(--green)}
.phone{left:440px;top:33px;display:flex;align-items:center;gap:8px;font-family:"Ubuntu",sans-serif;font-size:19px;color:#555;font-weight:500}
.phone .ico{width:24px;height:24px;background:var(--green);border-radius:4px;display:flex;align-items:center;justify-content:center}
.main-nav{left:681px;top:39px;display:flex;font-size:13.5px;color:#666}
.main-nav a{color:inherit;text-decoration:none;padding:0 10px}
.main-nav a+a{border-left:1px solid #bbb}
.main-nav a.active{color:var(--blue)}
.nav-marker{left:689px;top:87px;width:44px;height:4px;background:var(--blue)}

/* hero */
.hero{position:absolute;left:0;top:91px;width:1120px;height:388px;
  background:radial-gradient(ellipse at 30% 40%,#8cc24a 0%,#5f9a2a 45%,#3f7a1c 100%)}
.hero-person{left:700px;top:98px;width:260px;height:381px;border-radius:120px 120px 20px 20px;
  background:linear-gradient(180deg,#b07050 0%,#3a2a24 30%,#1c1a1c 100%);opacity:.9}
.hero-edge{left:0;top:471px;width:1120px;height:8px;
  background:linear-gradient(-45deg,#fff 4px,transparent 0),linear-gradient(45deg,#fff 4px,transparent 0);
  background-size:8px 8px;background-position:left bottom;background-repeat:repeat-x}
.hero-title{left:184px;top:196px;color:#fff;font-family:"Ubuntu Condensed","Roboto Condensed","Arial Narrow",sans-serif;font-weight:400;line-height:1;white-space:nowrap}
.hero-title .l1{display:block;font-size:42px}
.hero-title .l2{display:block;font-size:28px;margin-top:2px}
.search{left:184px;top:270px;width:527px;height:56px;background:linear-gradient(#fafafa,#ececec);border-radius:3px;box-shadow:0 1px 3px rgba(0,0,0,.3)}
.search-input{position:absolute;left:12px;top:15px;font-family:"Ubuntu",sans-serif;font-size:19px;color:#777}
.tld-select{position:absolute;left:332px;top:7px;width:90px;height:43px;background:linear-gradient(#f2f2f2,#dcdcdc);border:1px solid #ccc;border-radius:2px;font-family:"Ubuntu",sans-serif;font-size:18px;color:#555;display:flex;align-items:center;padding-left:12px;gap:14px}
.search-btn{position:absolute;left:430px;top:7px;width:91px;height:43px;background:linear-gradient(#2f7ad0,var(--blue-dark));border-radius:3px;display:flex;align-items:center;justify-content:center}
.adv-link{left:185px;top:331px;color:#fff;font-weight:700;font-size:13.5px}

/* offer */
.offer{left:182px;top:505px;width:740px;height:46px;background:var(--blue);border-radius:2px;overflow:hidden}
.offer-label{position:absolute;left:0;top:0;height:46px;width:205px;background:var(--green);color:#fff;font-family:"Ubuntu",sans-serif;font-weight:700;font-size:15.5px;line-height:46px;padding-left:13px;clip-path:polygon(0 0,195px 0,205px 50%,195px 100%,0 100%)}
.offer-text{position:absolute;left:232px;top:0;line-height:46px;color:#fff;font-size:14.5px}
.offer-btn{position:absolute;left:552px;top:6px;width:180px;height:33px;background:linear-gradient(#9ccb3c,#6f9d1d);border-radius:2px;font-family:"Ubuntu",sans-serif;font-weight:700;font-size:15px;color:#253a08;text-align:center;line-height:33px}

/* domains table */
.section-title{left:182px;top:583px;font-family:"Ubuntu",sans-serif;font-weight:500;font-size:28px;color:var(--blue)}
.domains{left:186px;top:622px;width:460px;border-collapse:collapse}
.domains th{font-family:"Ubuntu",sans-serif;font-weight:500;font-size:12px;color:#444;text-align:left;height:20px;padding:0}
.domains td{height:32px;font-size:13.5px;padding:0;vertical-align:middle;white-space:nowrap}
.domains .c1{width:202px}
.domains .c2{width:115px}
.domains .c3{width:95px}
.domains .name{font-weight:700;color:#444}
.domains .cat{color:#555}
.domains .price{color:var(--orange)}
.buy-btn{display:inline-block;width:48px;height:24px;line-height:22px;text-align:center;background:linear-gradient(#f2f2f2,#d8d8d8);border:1px solid #c4c4c4;border-radius:2px;font-size:11px;font-weight:700;color:#666}
.pager{left:186px;top:1038px;width:459px;height:32px;border:1px solid #ddd;border-radius:2px;background:linear-gradient(#fff,#f4f4f4);text-align:center;line-height:30px;font-size:13px;color:#888}

/* testimonial */
.testi-title{left:688px;top:592px;font-family:"Ubuntu",sans-serif;font-weight:700;font-size:15px;color:var(--green)}
.testi-quote{left:690px;top:620px}
.testi-who{left:745px;top:648px;font-size:13.5px;color:#666}
.testi-who b{font-weight:400;color:var(--blue)}
.testi-body{left:691px;top:677px;width:226px;font-style:italic;font-size:13px;line-height:19.2px;color:var(--quote)}

/* footer */
.footer-edge{left:0;top:1107px;width:1120px;height:8px;
  background:linear-gradient(-45deg,var(--blue-dark) 4px,transparent 0),linear-gradient(45deg,var(--blue-dark) 4px,transparent 0);
  background-size:8px 8px;background-position:left bottom;background-repeat:repeat-x}
.site-footer{left:0;top:1115px;width:1120px;height:85px;background:var(--blue-dark)}
.footer-links{left:193px;top:1144px;color:#fff;font-size:11.5px;display:flex;gap:11px}
.copyright{left:193px;top:1160px;color:var(--green);font-size:11.5px}
.address{left:525px;top:1142px;color:#fff;font-size:11.5px;line-height:15.5px;font-style:normal}
.footer-phone{left:796px;top:1139px;font-family:"Ubuntu",sans-serif;font-weight:500;font-size:20px;color:var(--green)}
</style>
</head>
<body>

<header class="site-header">
  <div class="abs brand"><span>ZEPRILO.COM</span><span class="dot"></span></div>
  <div class="abs phone">
    <span class="ico"><svg width="14" height="14" viewBox="0 0 24 24"><path fill="#fff" d="M6.6 10.8a15 15 0 0 0 6.6 6.6l2.2-2.2a1 1 0 0 1 1-.25 11.4 11.4 0 0 0 3.6.57 1 1 0 0 1 1 1V20a1 1 0 0 1-1 1A17 17 0 0 1 3 4a1 1 0 0 1 1-1h3.5a1 1 0 0 1 1 1c0 1.25.2 2.45.57 3.57a1 1 0 0 1-.25 1z"/></svg></span>
    +1 555.014.2290
  </div>
  <nav class="abs main-nav">
    <a class="active">Home</a><a>FAQS</a><a>About Us</a><a>Contact</a>
  </nav>
</header>
<div class="abs nav-marker"></div>

<section class="hero" role="img" aria-label="Photo of a sunlit green grass field"></section>
<div class="abs hero-person" role="img" aria-label="Photo of a smiling businesswoman in a dark suit holding a pen and folder"></div>
<div class="abs hero-edge"></div>

<h1 class="abs hero-title"><span class="l1">FIND A PREMIUM DOMAIN</span><span class="l2">AND GET MORE TRAFFIC TO YOUR SITE</span></h1>

<form class="abs search">
  <span class="search-input">Enter your domain name</span>
  <span class="tld-select">.com <svg width="11" height="8" viewBox="0 0 11 8"><path d="M0 0h11L5.5 8z" fill="#666"/></svg></span>
  <span class="search-btn"><svg width="32" height="28" viewBox="0 0 32 28"><circle cx="12" cy="12" r="9" fill="none" stroke="#fff" stroke-width="3.5"/><path d="M19 18l9 8" stroke="#fff" stroke-width="5" stroke-linecap="round"/></svg></span>
</form>
<a class="abs adv-link">Advanced Search</a>

<aside class="abs offer">
  <div class="offer-label">TODAY’S SPECIAL OFFER</div>
  <div class="offer-text">GET 25% OFF ON ALL PREMIUM DOMAINS</div>
  <div class="offer-btn">GRAB THE OFFER NOW</div>
</aside>

<h2 class="abs section-title">DOMAINS FOR SALE</h2>
<table class="abs domains">
  <thead><tr><th class="c1">DOMAIN</th><th class="c2">CATEGORY</th><th class="c3">PRICE</th><th></th></tr></thead>
  <tbody>
    <tr><td class="name">medivira.example</td><td class="cat">Health</td><td class="price">$8700.00</td><td><span class="buy-btn">Buy</span></td></tr>
    <tr><td class="name">teamwallets.example</td><td class="cat">Sports</td><td class="price">$5000.00</td><td><span class="buy-btn">Buy</span></td></tr>
    <tr><td class="name">motor-vintage.example</td><td class="cat">Vehicles</td><td class="price">$100.00</td><td><span class="buy-btn">Buy</span></td></tr>
    <tr><td class="name">newroadster.example</td><td class="cat">Vehicles</td><td class="price">$100.00</td><td><span class="buy-btn">Buy</span></td></tr>
    <tr><td class="name">bajarmelodias.example</td><td class="cat">Other</td><td class="price">$4397.00</td><td><span class="buy-btn">Buy</span></td></tr>
    <tr><td class="name">everyhomestead.example</td><td class="cat">Real Estate</td><td class="price">$999.00</td><td><span class="buy-btn">Buy</span></td></tr>
    <tr><td class="name">news-q.example</td><td class="cat">Media</td><td class="price">$197.00</td><td><span class="buy-btn">Buy</span></td></tr>
    <tr><td class="name">fabricasprocesos.example</td><td class="cat">Law</td><td class="price">$100.00</td><td><span class="buy-btn">Buy</span></td></tr>
    <tr><td class="name">plainloananswers.example</td><td class="cat">Finance</td><td class="price">$300.00</td><td><span class="buy-btn">Buy</span></td></tr>
    <tr><td class="name">ohyup.example</td><td class="cat">Other</td><td class="price">$211.00</td><td><span class="buy-btn">Buy</span></td></tr>
    <tr><td class="name">size22.example</td><td class="cat">Other</td><td class="price">$999.00</td><td><span class="buy-btn">Buy</span></td></tr>
    <tr><td class="name">refillplanet.example</td><td class="cat">Society</td><td class="price">$100.00</td><td><span class="buy-btn">Buy</span></td></tr>
  </tbody>
</table>
<div class="abs pager">‹ First « 1 2 3 4 5 6 7 8 9 » &nbsp;Last ›</div>

<h3 class="abs testi-title">WHAT OUR CLIENT’S SAY</h3>
<svg class="abs testi-quote" width="46" height="46" viewBox="0 0 46 46">
  <path d="M0 46V20C0 8 6 1 18 0v8c-6 1-9 5-9 12h9v26zM25 46V20C25 8 31 1 43 0v8c-6 1-9 5-9 12h9v26z" fill="#bdbdbd"/>
</svg>
<p class="abs testi-who"><b>calm-stretch.example</b> says</p>
<p class="abs testi-body">Excellent, responsive, service. The folks at Parcel Names Collective are knowledgeable and gaParcel Names Collectivee that I was buying my domain from a trustworthy organiza-tion.</p>

<div class="abs footer-edge"></div>
<footer class="abs site-footer"></footer>
<nav class="abs footer-links"><a>UNIVERSAL TERMS</a><a>REFUND POLICY</a><a>PRIVACY POLICY</a></nav>
<p class="abs copyright">© 2013 Zeprilo, Inc.</p>
<address class="abs address">1480 Larchmont Way, Suite 210 Brookfield,<br>ST 40120 United States</address>
<p class="abs footer-phone">+1 555.014.2290</p>

</body>
</html>
```